Lantern Advisory Business Cards

We need a new layout for our business cards. We have a logo already. But we might be interested in only using the Lantern portion of the logo. It has been uploaded.

We would like cards that are not overly busy. Clean. Modern. Perhaps a gray color for one side.

On the back, we would like to have the lantern part of the logo and "Take the Leap, we've got you!"

Our business provides medics and safety training for corporate clients. Our website is www.lanternadvisoryllc.example.

Industry/Entity Type

Business

Contact Information for Business Card

We want include name, email address, cell phone, main line number, and website URL on the front. Use the following as an example: Marla Tobin, marla@lanternadvisoryllc.example, 402.318.7264 (cell), 402.947.315, and www.lanternadvisoryllc.example.

Font styles to use
Serif
Sans Serif

Requirements
Must have
• All required information. Back side logo with "Take the leap, we will catch you!"
Nice to have
• If possible, we would like to consider creating a card in a non-standard shape. Perhaps, the shape of a lantern. Just interested in understanding the option.

```html
<!DOCTYPE html>
<html lang="en">
<head>
<meta charset="utf-8">
<title>Lantern Advisory – Card Back</title>
<link href="https://fonts.googleapis.com/css2?family=Comfortaa:wght@700&display=swap" rel="stylesheet">
<style>
  :root {
    --brand-blue: #144b85;
    --paper: #ffffff;
    --edge: #2b2b2b;
    --shade: #9a9a9a;
  }
  html, body {
    margin: 0;
    padding: 0;
    width: 1200px;
    height: 688px;
    overflow: hidden;
    background: var(--paper);
  }
  .card-back {
    position: relative;
    width: 1200px;
    height: 688px;
    background: var(--paper);
    font-family: "Comfortaa", sans-serif;
  }
  .card-corners {
    position: absolute;
    inset: 0;
  }
  .brand-name {
    position: absolute;
    left: 0;
    right: 0;
    top: 118px;
    margin: 0;
    text-align: center;
    color: var(--brand-blue);
    font-weight: 700;
    font-size: 64px;
    letter-spacing: 1px;
  }
  .tagline-band {
    position: absolute;
    left: 5px;
    right: 5px;
    top: 318px;
    height: 52px;
    background: var(--brand-blue);
  }
  .tagline {
    position: absolute;
    left: 146px;
    top: 0;
    margin: 0;
    line-height: 52px;
    color: var(--paper);
    font-weight: 700;
    font-size: 42px;
    letter-spacing: 5px;
    white-space: nowrap;
  }
</style>
</head>
<body>
  <main class="card-back">
    <svg class="card-corners" viewBox="0 0 1200 688" width="1200" height="688" aria-hidden="true">
      <defs>
        <filter id="curve-shade" x="-10%" y="-10%" width="120%" height="120%">
          <feGaussianBlur stdDeviation="4"/>
        </filter>
      </defs>
      <path d="M 960 5 Q 1150 20 1186 240" fill="none" stroke="var(--shade)" stroke-width="8" filter="url(#curve-shade)"/>
      <path d="M 968 5 Q 1158 20 1195 235 L 1195 5 Z" fill="var(--brand-blue)"/>
      <path d="M 14 452 Q 48 668 240 676" fill="none" stroke="var(--shade)" stroke-width="8" filter="url(#curve-shade)"/>
      <path d="M 5 458 Q 40 676 235 683 L 5 683 Z" fill="var(--brand-blue)"/>
      <rect x="4" y="4" width="1192" height="680" fill="none" stroke="var(--edge)" stroke-width="2"/>
    </svg>

    <p class="brand-name">Lantern</p>

    <div class="tagline-band">
      <p class="tagline">“Step Forward We’re with you!”</p>
    </div>
  </main>
</body>
</html>
```